RMT Electrical Business Card Design

Have a logo to use, just looking for design around this, would like green theme, would like symbols in place of phone, fax, email etc.

Business

Contact Information for Business Card

RMT Electrical, Simon Ashcroft, simon@rmtelectrical-example.com.au, www.rmtelectrical-example.com.au, mobile 0412 555 019, phone (07) 3555 0142, fax (07) 3555 0142, facebook and linkedin
addresses

```html
<!DOCTYPE html>
<html lang="en">
<head>
<meta charset="utf-8">
<title>RMT Electrical Business Card</title>
<link rel="stylesheet" href="https://fonts.googleapis.com/css2?family=Open+Sans:wght@400;600;700&display=swap">
<style>
  :root {
    --bg: #8d8e91;
    --card-front: #fbfcf3;
    --ink: #1c1c1c;
    --ink-soft: #2b2b2b;
    --green: #5cc24a;
    --green-dark: #3f9d34;
    --green-light: #8fdc7c;
    --grey-mid: #c4c4c3;
    --web-red: #c4262b;
  }
  * { box-sizing: border-box; margin: 0; padding: 0; }
  html, body { width: 1200px; height: 1200px; overflow: hidden; }
  body {
    background: var(--bg);
    font-family: "Open Sans", Arial, sans-serif;
    color: var(--ink);
    position: relative;
  }
  .card {
    position: absolute;
    left: 218px;
    width: 765px;
    height: 462px;
    border: 1px solid #7d7e80;
    box-shadow: 0 2px 6px rgba(0,0,0,0.25);
    overflow: hidden;
  }
  /* Front */
  .card--front {
    top: 119px;
    background: linear-gradient(90deg, #d4d6cf 0px, var(--card-front) 90px, var(--card-front) 100%);
  }
  .side-web {
    position: absolute;
    left: 22px;
    top: 70px;
    display: flex;
    align-items: center;
    gap: 10px;
    transform-origin: left top;
    transform: translate(34px, 0) rotate(90deg);
    font-size: 18px;
    color: var(--ink-soft);
    white-space: nowrap;
  }
  .web-icon { width: 18px; height: 18px; flex: none; transform: rotate(-90deg); }
  .side-brand {
    position: absolute;
    left: 164px;
    top: 52px;
    display: flex;
    align-items: center;
    gap: 14px;
    transform-origin: left top;
    transform: rotate(90deg);
    font-size: 44px;
    font-weight: 400;
    color: var(--ink);
    white-space: nowrap;
    letter-spacing: 0.5px;
  }
  .brand-dot {
    width: 44px; height: 44px; border-radius: 50%;
    background: var(--grey-mid);
    flex: none;
  }
  .holder-name {
    position: absolute;
    left: 484px;
    top: 46px;
    font-size: 20px;
    font-weight: 700;
    letter-spacing: 0.3px;
    color: var(--ink);
  }
  .name-bar {
    position: absolute;
    left: 484px;
    right: 0;
    top: 79px;
    height: 10px;
    background: linear-gradient(180deg, var(--green-light), var(--green) 55%, var(--green-dark));
  }
  .contact-list {
    position: absolute;
    right: 62px;
    top: 262px;
    list-style: none;
    text-align: right;
  }
  .contact-list li {
    display: flex;
    justify-content: flex-end;
    align-items: center;
    gap: 8px;
    height: 25.5px;
    font-size: 17px;
    color: var(--ink-soft);
  }
  .contact-icon { width: 21px; height: 21px; flex: none; }
  .social {
    position: absolute;
    left: 582px;
    top: 389px;
    display: flex;
    gap: 19px;
  }
  .social-tile {
    width: 32px; height: 32px;
    border-radius: 5px;
    background: linear-gradient(180deg, var(--green-light), var(--green-dark));
    border: 1px solid var(--green-dark);
  }
  /* Back */
  .card--back {
    top: 593px;
    background: radial-gradient(ellipse at 50% 45%, #fafafa 0%, #dcdcdb 45%, #b9b9b8 100%);
  }
  .back-band {
    position: absolute;
    left: 0; right: 0;
    top: 134px;
    height: 173px;
    background: linear-gradient(180deg, var(--green) 0%, var(--green-light) 50%, var(--green) 100%);
    display: flex;
    align-items: center;
    justify-content: center;
    gap: 22px;
  }
  .back-brand {
    font-size: 76px;
    font-weight: 400;
    color: var(--ink);
    letter-spacing: 1px;
  }
  .back-band .brand-dot { width: 84px; height: 84px; background: #8a8a8a; }
  .back-web {
    position: absolute;
    left: 0; right: 0;
    top: 410px;
    display: flex;
    justify-content: center;
    align-items: center;
    gap: 9px;
    font-size: 20px;
    color: var(--ink-soft);
  }
  .back-web .web-icon { transform: none; }
</style>
</head>
<body>

<section class="card card--front" aria-label="Business card front">
  <div class="side-web">
    <svg class="web-icon" viewBox="0 0 20 20" aria-hidden="true">
      <circle cx="10" cy="10" r="9" fill="var(--web-red)"/>
      <g fill="none" stroke="#fff" stroke-width="1.2">
        <ellipse cx="10" cy="10" rx="4" ry="8"/>
        <line x1="2" y1="10" x2="18" y2="10"/>
        <line x1="10" y1="2" x2="10" y2="18"/>
      </g>
    </svg>
    <span>www.rmtelectrical-example.com.au</span>
  </div>

  <div class="side-brand">
    <span class="brand-dot" aria-hidden="true"></span>
    <span>RMT Electrical</span>
  </div>

  <h1 class="holder-name">SIMON ASHCROFT</h1>
  <div class="name-bar" aria-hidden="true"></div>

  <ul class="contact-list">
    <li><span>0412 555 019</span>
      <svg class="contact-icon" viewBox="0 0 22 22" aria-label="Mobile"><circle cx="11" cy="11" r="10" fill="var(--green)"/><rect x="8" y="5" width="6" height="12" rx="1" fill="none" stroke="#fff" stroke-width="1.4"/><line x1="10" y1="15" x2="12" y2="15" stroke="#fff" stroke-width="1.2"/></svg></li>
    <li><span>(07) 3555 0142</span>
      <svg class="contact-icon" viewBox="0 0 22 22" aria-label="Phone"><circle cx="11" cy="11" r="10" fill="var(--green)"/><path d="M7 6c-1 1 0 5 3 8s7 4 8 3l-2-3-2 1c-1-.5-3-2.5-3.5-3.5l1-2z" fill="#fff"/></svg></li>
    <li><span>(07) 3555 0142</span>
      <svg class="contact-icon" viewBox="0 0 22 22" aria-label="Fax"><circle cx="11" cy="11" r="10" fill="var(--green)"/><rect x="8" y="5" width="6" height="4" fill="#fff"/><rect x="5.5" y="9" width="11" height="6" rx="1" fill="#fff"/><rect x="8" y="13" width="6" height="4" fill="#fff" stroke="var(--green)" stroke-width="0.8"/></svg></li>
    <li><span>simon@rmtelectrical-example.com.au</span>
      <svg class="contact-icon" viewBox="0 0 22 22" aria-label="Email"><circle cx="11" cy="11" r="10" fill="var(--green)"/><rect x="5" y="7" width="12" height="8" fill="#fff"/><path d="M5 7l6 5 6-5" fill="none" stroke="var(--green)" stroke-width="1.2"/></svg></li>
  </ul>

  <div class="social" aria-label="Social profiles">
    <span class="social-tile" role="img" aria-label="Social profile link"></span>
    <span class="social-tile" role="img" aria-label="Professional profile link"></span>
  </div>
</section>

<section class="card card--back" aria-label="Business card back">
  <div class="back-band">
    <span class="brand-dot" aria-hidden="true"></span>
    <span class="back-brand">RMT Electrical</span>
  </div>
  <div class="back-web">
    <svg class="web-icon" viewBox="0 0 20 20" aria-hidden="true">
      <circle cx="10" cy="10" r="9" fill="var(--web-red)"/>
      <g fill="none" stroke="#fff" stroke-width="1.2">
        <ellipse cx="10" cy="10" rx="4" ry="8"/>
        <line x1="2" y1="10" x2="18" y2="10"/>
        <line x1="10" y1="2" x2="10" y2="18"/>
      </g>
    </svg>
    <span>www.rmtelectrical-example.com.au</span>
  </div>
</section>

</body>
</html>
```